Stationary Design for Medical Distribution Company

We are a Medical Distribution Company based in Dar es salaam, Tanzania (East Africa). Our company was established in 1995 and we are a reputed and respected Pharmaceuticals and Medical Supplies company in the region.
We have just recently changed our company logo. A new company logo has just recently been selected through Pixel Forum and we are now looking for stationary designs such as Business Cards, Letterheads, Envelopes, etc.. for our company.
We request you all to take a look at the attached new company logo and give us your best possible designs.
We would prefer to have a double sided business card. For letterheads, we are open to your ideas/designs.
We are looking forward for your designs!
Updates
Company details to be incorporated in designs:
Company Name: VELMO PHARMACEUTICALS LIMITED
Company Address: Office # 42, Kiteo Works Ltd., Mwangaza Road, Dar es salaam, Tanzania
Tel: +255 22 2917438 / 39, Fax: +255 22 2917440
Email: info@velmopharm.example
Website: www.velmopharm.example
Also should include Cell number +255 XXX XXX XXX
Name and Designation.....
Target Market(s)
Medical Sector
Industry/Entity Type
Medical
Look and feel

```html
<!DOCTYPE html>
<html lang="en">
<head>
<meta charset="utf-8">
<title>Velmo Pharmaceuticals Limited – Letterhead</title>
<link rel="stylesheet" href="https://fonts.googleapis.com/css2?family=Open+Sans:wght@400&family=Oswald:wght@600&family=Tinos&display=swap">
<style>
  :root {
    --paper: #ffffff;
    --blush: #f2dcdc;
    --blush-soft: #f8eaea;
    --brand-red: #c43c3c;
    --ink: #111111;
    --name-grey: #3a3a3a;
  }
  html, body {
    margin: 0;
    padding: 0;
    width: 927px;
    height: 1200px;
    overflow: hidden;
    background: var(--paper);
  }
  .letterhead {
    position: relative;
    width: 927px;
    height: 1200px;
    background: var(--paper);
    overflow: hidden;
  }
  .page-frame {
    position: absolute;
    left: 47px;
    top: 47px;
    width: 835px;
    height: 1105px;
    box-sizing: border-box;
    border: 7px solid var(--blush);
  }
  .backdrop-texture {
    position: absolute;
    left: 54px;
    top: 54px;
    width: 821px;
    height: 1091px;
    background: linear-gradient(150deg, var(--blush-soft) 0%, var(--paper) 45%, var(--blush-soft) 100%);
  }

  .brand {
    position: absolute;
    left: 417px;
    top: 72px;
    display: flex;
    align-items: flex-start;
  }
  .brand-square {
    width: 118px;
    height: 118px;
    border-radius: 9px;
    background: var(--brand-red);
  }
  .brand-name {
    margin-left: 11px;
    margin-top: -2px;
    font-family: "Open Sans", sans-serif;
    font-weight: 400;
    font-size: 35px;
    line-height: 37px;
    color: var(--name-grey);
  }

  .address {
    position: absolute;
    left: 562px;
    top: 206px;
    font-family: "Oswald", sans-serif;
    font-weight: 600;
    font-style: normal;
    font-size: 21px;
    line-height: 29.7px;
    color: var(--ink);
    letter-spacing: 0.4px;
  }
  .address p { margin: 0; }

  .body-copy {
    position: absolute;
    left: 76px;
    top: 404px;
    width: 800px;
    font-family: "Tinos", serif;
    font-size: 18.2px;
    line-height: 21px;
    color: var(--ink);
  }
  .body-copy p { margin: 0 0 21px; }
  .body-copy .indent { padding-left: 4px; }
  .body-copy .signoff { margin-top: 42px; }

  .established {
    position: absolute;
    right: 72px;
    top: 1104px;
    font-family: "Oswald", sans-serif;
    font-weight: 600;
    font-size: 21px;
    line-height: 30px;
    color: var(--ink);
    letter-spacing: 0.4px;
  }
</style>
</head>
<body>
<main class="letterhead">
  <div class="backdrop-texture" role="img" aria-label="Soft pale pink abstract background decoration"></div>
  <div class="page-frame"></div>

  <header class="brand">
    <div class="brand-square"></div>
    <div class="brand-name">Velmo<br>Pharmaceuticals<br>Limited</div>
  </header>

  <address class="address">
    <p>Office #42</p>
    <p>Kiteo Works Ltd.</p>
    <p>Mwangaza Road</p>
    <p>Dar es salaam</p>
    <p>Tanzania</p>
  </address>

  <section class="body-copy">
    <p>We are a Medical Distribution Company based in Dar es salaam, Tanzania (East Africa). .<br>
    Our company was established in 1995 and we are a reputed and respected Pharmaceuticals<br>
    <span class="indent">and Medical Supplies company in the region.</span></p>
    <p>We have just recently changed our company logo. A new company logo has just recently<br>
    <span class="indent">been selected through Pixel Forum and we are now looking for stationary designs such</span><br>
    <span class="indent">as Business Cards, Letterheads, Envelopes, etc.. for our company.</span></p>
    <p>We request you all to take a look at the attached new company logo and give us your best possible designs.</p>
    <p>We would prefer to have a double sided business card. For letterheads, we are open to your ideas/designs.</p>
    <p>We are looking forward to your designs</p>
    <p class="signoff">Sincerely, Ruth M. Kellaway</p>
  </section>

  <footer class="established">Established 1995</footer>
</main>
</body>
</html>
```